Glimmora Pages with Bold Font

I want the font to be simple yet bold for Glimmora images. Its all about a simple bold readable font. I need a single glimmora page with an image and copy/text on or over the image. The words will change in the future. I'm looking for the right font. I like fiery red and yellow colors. The "One Pic" attached is a sample of what I want without the Veltrix words.

```html
<!DOCTYPE html>
<html lang="en">
<head>
<meta charset="UTF-8">
<title>Maya Sol Brant – Trainer for Men</title>
<link href="https://fonts.googleapis.com/css2?family=Arimo:wght@700&display=swap" rel="stylesheet">
<style>
  :root {
    --red-deep: #6e0006;
    --red-main: #c5000c;
    --red-bright: #ff1a1f;
    --wave-dark: #8d0008;
    --lime-top: #d8f56a;
    --lime-bottom: #8fd82e;
    --text-light: #f4f4f4;
    --text-label: #e6e6e6;
    --skin-light: #e8b48c;
    --skin-mid: #c98a62;
  }
  html, body {
    margin: 0;
    padding: 0;
    overflow: hidden;
    background: #222;
  }
  .poster {
    position: relative;
    width: 1200px;
    height: 1200px;
    overflow: hidden;
    font-family: "Arimo", Arial, sans-serif;
    font-weight: 700;
    background: radial-gradient(ellipse at 70% 40%, var(--red-bright) 0%, var(--red-main) 45%, var(--red-deep) 100%);
  }
  .poster__waves {
    position: absolute;
    inset: 0;
    width: 1200px;
    height: 1200px;
  }
  .poster__photo {
    position: absolute;
    left: 0;
    top: 60px;
    width: 590px;
    height: 1140px;
    background: linear-gradient(180deg, #e9d08a 0%, var(--skin-light) 35%, var(--skin-mid) 100%);
    border-radius: 260px 260px 0 0;
    opacity: 0.92;
  }
  .poster__brand {
    position: absolute;
    top: 16px;
    right: 30px;
    margin: 0;
    font-size: 33px;
    color: var(--text-label);
    text-shadow: 1px 2px 3px rgba(0,0,0,0.45);
  }
  .poster__headline {
    position: absolute;
    top: 92px;
    left: 0;
    margin: 0;
    font-size: 66px;
    line-height: 80px;
    letter-spacing: -0.5px;
  }
  .poster__headline span {
    display: block;
    white-space: nowrap;
    background: linear-gradient(180deg, var(--lime-top), var(--lime-bottom));
    -webkit-background-clip: text;
    background-clip: text;
    color: transparent;
    filter: drop-shadow(2px 3px 2px rgba(60,0,0,0.55));
  }
  .poster__headline .line-1 { padding-left: 383px; }
  .poster__headline .line-2 { padding-left: 458px; }
  .poster__headline .line-3 { padding-left: 592px; }
  .poster__copy {
    position: absolute;
    top: 458px;
    left: 586px;
    width: 590px;
    color: var(--text-light);
    font-size: 40px;
    line-height: 56px;
    text-shadow: 2px 3px 4px rgba(0,0,0,0.55);
  }
  .poster__copy p {
    margin: 0 0 60px;
  }
  .poster__social {
    position: absolute;
    right: 40px;
    bottom: 38px;
    display: flex;
    gap: 22px;
    font-size: 24px;
    color: var(--text-light);
  }
  .poster__social-item {
    display: flex;
    align-items: center;
    gap: 8px;
  }
  .poster__social-dot {
    width: 14px;
    height: 14px;
    border-radius: 50%;
    background: var(--text-light);
  }
</style>
</head>
<body>
  <main class="poster">
    <svg class="poster__waves" viewBox="0 0 1200 1200" aria-hidden="true">
      <path d="M0 260 C 300 120, 700 60, 1200 0 L 1200 90 C 800 140, 380 230, 0 360 Z" fill="var(--wave-dark)" opacity="0.45"/>
      <path d="M520 1200 C 700 1000, 950 900, 1200 860 L 1200 1200 Z" fill="var(--wave-dark)" opacity="0.5"/>
      <path d="M0 900 C 300 820, 700 980, 1200 760 L 1200 820 C 720 1040, 300 880, 0 960 Z" fill="var(--red-bright)" opacity="0.25"/>
    </svg>

    <div class="poster__photo" role="img" aria-label="Photo of a blonde fitness model in a white bikini"></div>

    <h2 class="poster__brand">Maya Sol Brant Trainer for Men</h2>

    <h1 class="poster__headline">
      <span class="line-1">Wanna lose weight?</span>
      <span class="line-2">Wanna shrink that gut?</span>
      <span class="line-3">I can help you.</span>
    </h1>

    <div class="poster__copy">
      <p>The secret is to find what<br>works for YOU !</p>
      <p>&nbsp;And I can give you that !</p>
      <p>&nbsp;The pounds will melt<br>&nbsp;away, your guts will<br>&nbsp;shrink, and your health<br>will improve.</p>
    </div>

    <nav class="poster__social">
      <span class="poster__social-item"><span class="poster__social-dot"></span>Glimmora</span>
      <span class="poster__social-item"><span class="poster__social-dot"></span>Nexfolk</span>
      <span class="poster__social-item"><span class="poster__social-dot"></span>Chirpwave</span>
    </nav>
  </main>
</body>
</html>
```